Simple proffessional BC

I have a logo which I will attach below.
I would like the logo on the front of the card with these details in point form below:
Pre and Post Natal Yoga: Pregnancy Workshops: Hypnobirthing Courses
On the back of the card my details:
Merrin Galvey
Facebook page- calmbellieswillowharbour
Mobile- 0438 512 740

I like the idea of the card being simple, possibly just the above on a plain coloured (eggshell?) card, a card that is textured.
I am open to suggestion if it appeals!
Thank you and good luck!

Target Market(s)

Pregnant women, 20's-40's

Requirements
Must have
• Simple, compliment logo.
Make logo the feature.
Should not have

• .

```html
<!DOCTYPE html>
<html lang="en">
<head>
<meta charset="utf-8">
<title>Calm Bellies – Business Card</title>
<link href="https://fonts.googleapis.com/css2?family=Jost:wght@400;600&display=swap" rel="stylesheet">
<style>
  :root {
    --bg: #7a0003;
    --maroon: #5c0b12;
    --maroon-deep: #650006;
    --orange: #ef9a12;
    --orange-light: #f0c97e;
    --white: #ffffff;
  }
  * { margin: 0; padding: 0; box-sizing: border-box; }
  html, body {
    width: 1200px;
    height: 1000px;
    overflow: hidden;
    background: var(--bg);
    font-family: "Jost", "Century Gothic", sans-serif;
  }
  .canvas {
    position: relative;
    width: 1200px;
    height: 1000px;
  }
  .card {
    position: absolute;
    left: 220px;
    width: 760px;
    height: 420px;
    overflow: hidden;
    box-shadow: 0 6px 18px rgba(0,0,0,0.3);
  }

  /* Back of card */
  .card-back {
    top: 60px;
    background: radial-gradient(ellipse at 50% 45%, var(--orange-light) 0%, #f0b54a 55%, var(--orange) 100%);
    color: var(--maroon);
  }
  .contact {
    position: absolute;
    left: 0;
    right: 0;
    top: 250px;
    text-align: center;
    line-height: 1.25;
  }
  .contact-name {
    font-weight: 600;
    font-size: 24px;
  }
  .contact-line {
    font-size: 20px;
  }

  /* Front of card */
  .card-front {
    top: 520px;
    background: var(--white);
    color: var(--maroon);
  }
  .brand {
    position: absolute;
    left: 56px;
    top: 48px;
    display: flex;
    align-items: center;
    gap: 14px;
  }
  .brand-dot {
    width: 52px;
    height: 52px;
    border-radius: 50%;
    background: var(--orange);
  }
  .brand-name {
    font-size: 38px;
    font-weight: 400;
    color: var(--maroon);
  }
  .services {
    position: absolute;
    right: 60px;
    top: 230px;
    list-style: none;
    font-size: 21px;
    line-height: 1.4;
  }
  .services li {
    display: flex;
    align-items: center;
    gap: 10px;
  }
  .bullet { width: 12px; height: 12px; flex: none; }
  .footer-band {
    position: absolute;
    left: 0;
    bottom: 0;
    width: 760px;
    height: 20px;
  }
</style>
</head>
<body>
<main class="canvas">
  <section class="card card-back" aria-label="Back of card">
    <div class="contact">
      <p class="contact-name">Merrin Galvey</p>
      <p class="contact-line">facebook Page : calmbellieswillowharbour</p>
      <p class="contact-line">Mobile : 0438 512 740</p>
    </div>
  </section>

  <section class="card card-front" aria-label="Front of card">
    <div class="brand">
      <span class="brand-dot"></span>
      <span class="brand-name">Calm Bellies</span>
    </div>

    <ul class="services">
      <li>
        <svg class="bullet" viewBox="0 0 12 12" aria-hidden="true">
          <g transform="rotate(45 6 6)">
            <rect x="2" y="2" width="3.8" height="3.8" fill="var(--maroon)"/>
            <rect x="6.2" y="2" width="3.8" height="3.8" fill="var(--orange)"/>
            <rect x="2" y="6.2" width="3.8" height="3.8" fill="var(--orange)"/>
            <rect x="6.2" y="6.2" width="3.8" height="3.8" fill="var(--maroon)"/>
          </g>
        </svg>
        Pre and Post Natal Yoga
      </li>
      <li>
        <svg class="bullet" viewBox="0 0 12 12" aria-hidden="true">
          <g transform="rotate(45 6 6)">
            <rect x="2" y="2" width="3.8" height="3.8" fill="var(--maroon)"/>
            <rect x="6.2" y="2" width="3.8" height="3.8" fill="var(--orange)"/>
            <rect x="2" y="6.2" width="3.8" height="3.8" fill="var(--orange)"/>
            <rect x="6.2" y="6.2" width="3.8" height="3.8" fill="var(--maroon)"/>
          </g>
        </svg>
        Pregnancy Workshops
      </li>
      <li>
        <svg class="bullet" viewBox="0 0 12 12" aria-hidden="true">
          <g transform="rotate(45 6 6)">
            <rect x="2" y="2" width="3.8" height="3.8" fill="var(--maroon)"/>
            <rect x="6.2" y="2" width="3.8" height="3.8" fill="var(--orange)"/>
            <rect x="2" y="6.2" width="3.8" height="3.8" fill="var(--orange)"/>
            <rect x="6.2" y="6.2" width="3.8" height="3.8" fill="var(--maroon)"/>
          </g>
        </svg>
        Hypnobirthing Courses
      </li>
    </ul>

    <svg class="footer-band" viewBox="0 0 760 20" aria-hidden="true">
      <polygon points="0,0 120,0 128,20 0,20" fill="var(--maroon-deep)"/>
      <polygon points="126,0 760,0 760,20 134,20" fill="var(--orange)"/>
    </svg>
  </section>
</main>
</body>
</html>
```